Gift Card Design - Suds Harbor Lane

I am needing a design for a standard plastic gift card, (ever so slightly large then a standard rounded edge business card). Name of the business is Suds Harbor Lane. Attached is a file with a poor example, done by an equipment manufacturing firm, that I feel could be much better. Simple, clean and classy with what it is and does along with our name is what I am looking for. Attached also is out logo and source of logo, they don't have to be on the card.

Target Market(s)

Car wash customers in an upscale market.

Industry/Entity Type

Business

Font styles to use
Serif
Other font styles liked:
• whatever you feel, but I do like the font on a Verlance golf ball

Requirements
Must have
• Words anywhere on the card -
• Reloadable Card
• Self Serve Bays & Vacuums.
• Also need name of the business, Suds Harbor Lane.
Nice to have
• Work in Pantone #7483 as there is existing signage with that as a primary color, just trying to tie things together. Attached is my business logo and a picture of the source of the logo, you do not have to use those if you don't want to. I do like clean and classy but am open to creativity, that's why I am submitting this project.
Should not have
• Naked lady pictures

```html
<!DOCTYPE html>
<html lang="en">
<head>
<meta charset="UTF-8">
<title>Suds Harbor Lane – Reloadable Card</title>
<link rel="stylesheet" href="https://fonts.googleapis.com/css2?family=Playfair+Display:wght@700&family=Fira+Sans:wght@500&display=swap">
<style>
  :root {
    --backdrop: #e9ebe8;
    --card-white: #ffffff;
    --pine: #23603a;
    --teal: #2f9c89;
    --teal-mist: #d6efe9;
    --ink: #1c1a19;
  }
  * { box-sizing: border-box; margin: 0; padding: 0; }
  html, body {
    width: 1200px;
    height: 800px;
    overflow: hidden;
    background: var(--backdrop);
  }
  .canvas {
    position: relative;
    width: 1200px;
    height: 800px;
  }
  .gift-card {
    position: absolute;
    left: 100px;
    top: 90px;
    width: 1000px;
    height: 620px;
    border-radius: 36px;
    overflow: hidden;
    background: var(--card-white);
    box-shadow: 0 6px 24px rgba(0,0,0,0.18);
  }
  .wave-art {
    position: absolute;
    left: 0;
    top: 230px;
    width: 100%;
    height: 240px;
    background: linear-gradient(172deg,
      var(--card-white) 0%,
      var(--teal-mist) 35%,
      var(--teal) 70%,
      var(--pine) 100%);
  }
  .service-band {
    position: absolute;
    left: 0;
    top: 470px;
    width: 100%;
    height: 150px;
    background: var(--pine);
  }
  .business-name {
    position: absolute;
    top: 56px;
    left: 0;
    width: 100%;
    text-align: center;
    font-family: "Playfair Display", Georgia, serif;
    font-weight: 700;
    font-size: 70px;
    line-height: 1;
    letter-spacing: 0.5px;
    text-transform: uppercase;
    color: var(--ink);
  }
  .card-type {
    position: absolute;
    top: 150px;
    left: 0;
    width: 100%;
    text-align: center;
    font-family: "Fira Sans", "Trebuchet MS", sans-serif;
    font-weight: 500;
    font-size: 46px;
    line-height: 1;
    color: var(--pine);
  }
  .services {
    position: absolute;
    left: 104px;
    top: 524px;
    font-family: "Fira Sans", "Trebuchet MS", sans-serif;
    font-weight: 500;
    font-size: 42px;
    line-height: 1;
    color: var(--card-white);
  }
  .name-tile {
    position: absolute;
    left: 852px;
    top: 468px;
    width: 120px;
    height: 120px;
    border-radius: 18px;
    background: var(--card-white);
    display: flex;
    align-items: center;
    justify-content: center;
    text-align: center;
    padding: 10px;
    font-family: "Playfair Display", Georgia, serif;
    font-weight: 700;
    font-size: 19px;
    line-height: 1.15;
    color: var(--pine);
  }
</style>
</head>
<body>
<main class="canvas">
  <section class="gift-card" aria-label="Suds Harbor Lane reloadable card">
    <div class="wave-art" role="img" aria-label="Flowing green and teal water wave decoration"></div>
    <div class="service-band"></div>
    <h1 class="business-name">Suds Harbor Lane</h1>
    <p class="card-type">Reloadable Card</p>
    <p class="services">Self Serve Bays &amp; Vacuums</p>
    <div class="name-tile">Suds Harbor Lane</div>
  </section>
</main>
</body>
</html>
```